A new company focused on starting and investing in transformative businesses.

We need a simple and clean website with a few pages. we like larkmeadow.com as a starting point. we want the landing page to be very simple with an option to click through on the top right into INVESTOR LOGIN. then we want to be able to scroll down to see more about our company.

Target Market(s)

professional

Coding

Coded - Design and coding required

Number of Pages Required

2 page

Font styles to use
Serif
Sans Serif

Requirements
Must have
• HALVERN BUILDERS logo (attached as a file) on the top with INVESTOR LOGIN as a click through on the right. Please model the click through from larkmeadow.com. The description (also written in attached file) should be on the landing page. we do not want to have to scroll to read the description.

Then we can scroll down to read more about Halvern including the mission and the two types of businesses. More is detailed on the attached file called "Halvern Website Syntax"
Should not have
• should not be slow loading with lots of fancy graphics. should not be busy and with too many colors.

```html
<!DOCTYPE html>
<html lang="en">
<head>
<meta charset="UTF-8">
<title>Halvern Builders</title>
<link href="https://fonts.googleapis.com/css2?family=Montserrat:wght@400;500;600;700&display=swap" rel="stylesheet">
<style>
:root{
  --brand:#0a5aa0;
  --ink:#111111;
  --text:#222222;
  --hero-bg:#ececec;
  --soft-bg:#f5f6f8;
  --white:#ffffff;
  --footer:#000000;
  --rule:#333333;
}
*{margin:0;padding:0;box-sizing:border-box}
html,body{width:743px;height:1200px;overflow:hidden;background:var(--white)}
body{font-family:"Montserrat",sans-serif;color:var(--text)}
.page{position:relative;width:743px;height:1200px;overflow:hidden}
.abs{position:absolute}

.hero-bg{left:0;top:0;width:743px;height:322px;
  background:radial-gradient(circle at 30% 20%,#f6f6f6 0,#e9e9e9 40%,transparent 70%),
             radial-gradient(circle at 75% 60%,#f4f4f4 0,#e6e6e6 45%,transparent 75%),
             linear-gradient(180deg,#eeeeee,#f2f2f2)}
.brand{left:87px;top:17px;display:flex;align-items:center;gap:7px}
.brand-mark{width:30px;height:36px;background:var(--brand)}
.brand-name{font-weight:500;font-size:14.5px;line-height:16px;color:#1a1a1a;letter-spacing:.3px}
.login{left:564px;top:22px;width:91px;height:25px;border:1px solid var(--brand);border-radius:13px;
  color:var(--brand);font-size:8px;font-weight:600;letter-spacing:.3px;display:flex;align-items:center;justify-content:center;text-decoration:none}
.hero-title{left:0;width:743px;top:111px;text-align:center;color:var(--brand);font-weight:700;font-size:24.5px;letter-spacing:.4px}
.hero-sub{left:0;width:743px;top:147px;text-align:center;font-size:10.8px;line-height:18px;color:#1a1a1a;font-weight:500}
.btn{height:24px;width:109px;left:317px;border-radius:12px;background:var(--brand);color:var(--white);
  font-size:7.8px;font-weight:600;letter-spacing:.4px;display:flex;align-items:center;justify-content:center;text-decoration:none}

.soft-bg{left:0;top:678px;width:743px;height:420px}
.section-title{left:0;width:743px;text-align:center;font-weight:700;font-size:19.6px;color:var(--ink)}
.mission-text{left:0;width:743px;top:386px;text-align:center;font-size:13.3px;line-height:21px;color:#1a1a1a}

.card{left:87px;top:449px;width:568px;height:196px;background:var(--white);border-radius:6px;box-shadow:0 2px 12px rgba(0,0,0,.07)}
.feature{position:absolute;top:20px;width:180px}
.feature-icon{width:44px;height:40px}
.feature h3{margin-top:8px;font-size:12.8px;font-weight:700;color:var(--ink)}
.feature p{margin-top:6px;font-size:7.6px;line-height:14.2px;color:#222}
.emblem{position:absolute;left:208px;top:21px;width:153px;height:153px;border-radius:50%;background:var(--brand);
  display:flex;align-items:center;justify-content:center;color:var(--white);font-weight:700;font-size:17px;letter-spacing:1px}

.team{left:87px;top:791px;display:flex;gap:9px}
.member{width:135.5px;height:183px;background:var(--white);position:relative;box-shadow:0 1px 6px rgba(0,0,0,.05)}
.portrait{position:absolute;left:0;top:0;width:100%;height:135px;clip-path:polygon(0 0,100% 0,100% 118px,0 135px)}
.member h4{position:absolute;top:144px;width:100%;text-align:center;font-size:9.5px;font-weight:600;color:var(--ink)}
.member span{position:absolute;top:160px;width:100%;text-align:center;font-size:7.5px;color:#222}

.contact{top:1109px;display:flex;gap:12px}
.contact-icon{width:24px;height:24px;background:var(--brand);display:flex;align-items:center;justify-content:center}
.contact-label{color:var(--white);font-size:9px;font-weight:500;letter-spacing:.3px;margin-top:3px}
.contact-value{color:var(--white);font-size:9px;margin-top:4px;line-height:11.5px}
.contact-value.small{font-size:7.8px}
.rule{left:87px;top:1163px;width:568px;height:1px;background:var(--rule)}
.copyright{left:0;width:743px;top:1176px;text-align:center;color:#dddddd;font-size:7.5px}
.copyright b{color:var(--white);font-weight:700}
</style>
</head>
<body>
<div class="page">

  <div class="abs hero-bg" role="img" aria-label="Soft grey abstract background with faint rings"></div>
  <svg class="abs" style="left:0;top:285px" width="743" height="40" viewBox="0 0 743 40">
    <polygon points="0,36 743,5 743,18 0,40" fill="#0a5aa0"/>
    <polygon points="0,37 743,18 743,40 0,40" fill="#ffffff"/>
  </svg>

  <div class="abs brand"><div class="brand-mark"></div><div class="brand-name">HALVERN<br>BUILDERS</div></div>
  <a class="abs login" href="#">INVESTOR LOGIN</a>

  <h1 class="abs hero-title">HALVERN BUILDERS</h1>
  <p class="abs hero-sub">Is An Entrepreneurial Firm Focused On Building And<br>Growing Transformational Companies</p>
  <a class="abs btn" style="top:193px" href="#">CONTACT US TODAY</a>

  <h2 class="abs section-title" style="top:354px">Our Mission</h2>
  <p class="abs mission-text">Mission Is To Build Meaningful Businesses That Create Enduring Value By<br>Impacting People In A Measurable Way.</p>

  <div class="abs card">
    <div class="feature" style="left:15px">
      <svg class="feature-icon" viewBox="0 0 44 40">
        <circle cx="19" cy="20" r="19" fill="#e8eef6"/>
        <g fill="none" stroke="#0a5aa0" stroke-width="1.3">
          <rect x="10" y="30" width="4" height="7"/><rect x="17" y="26" width="4" height="11"/>
          <rect x="24" y="22" width="4" height="15"/><rect x="31" y="17" width="4" height="20"/>
          <polyline points="9,25 16,18 21,21 31,11"/><polyline points="27,11 31,11 31,15"/>
          <circle cx="38" cy="9" r="4"/>
        </g>
        <line x1="8" y1="37.5" x2="37" y2="37.5" stroke="#0a5aa0" stroke-width="1.3"/>
      </svg>
      <h3>Ground Up</h3>
      <p>Our ground up business applies a proven analytic process to identify value edge, a form of competitive advantage. We architect transformational companies and are deliberate in creating the foundation necessary to lead an industry.</p>
    </div>
    <div class="emblem">HALVERN</div>
    <div class="feature" style="left:379px">
      <svg class="feature-icon" viewBox="0 0 44 40">
        <circle cx="19" cy="20" r="19" fill="#e8eef6"/>
        <g fill="none" stroke="#0a5aa0" stroke-width="1.3">
          <rect x="9" y="5" width="20" height="26"/>
          <line x1="14" y1="18" x2="14" y2="13"/><line x1="18" y1="18" x2="18" y2="10"/><line x1="22" y1="18" x2="22" y2="12"/>
          <circle cx="22" cy="30" r="6"/><rect x="29" y="27" width="11" height="8"/>
          <line x1="34" y1="27" x2="34" y2="17"/><path d="M34 20 q4 -4 7 -3"/>
        </g>
      </svg>
      <h3>Special Opportunities</h3>
      <p>We partner with exceptional teams that create value by transforming lives. Our investment focus includes large companies and spin-outs.</p>
    </div>
  </div>

  <svg class="abs" style="left:0;top:678px" width="743" height="422" viewBox="0 0 743 422">
    <polygon points="0,39 743,0 743,422 0,422" fill="#f5f6f8"/>
  </svg>

  <h2 class="abs section-title" style="top:745px">Halvern Builders</h2>

  <div class="abs team">
    <div class="member"><div class="portrait" role="img" aria-label="Portrait photo of Owen Hartley" style="background:linear-gradient(180deg,#dcdcdc,#c9cbd0)"></div><h4>Owen Hartley</h4><span>Designation</span></div>
    <div class="member"><div class="portrait" role="img" aria-label="Portrait photo of Maris Calloway" style="background:linear-gradient(180deg,#d6d6d6,#b49a86)"></div><h4>Maris Calloway</h4><span>Designation</span></div>
    <div class="member"><div class="portrait" role="img" aria-label="Portrait photo of Nadia Ferrel" style="background:linear-gradient(180deg,#ececec,#a88a74)"></div><h4>Nadia Ferrel</h4><span>Designation</span></div>
    <div class="member"><div class="portrait" role="img" aria-label="Portrait photo of Declan Moss" style="background:linear-gradient(180deg,#e3f3fb,#b9d4ee)"></div><h4>Declan Moss</h4><span>Designation</span></div>
  </div>

  <a class="abs btn" style="top:999px" href="#">CONTACT US TODAY</a>

  <svg class="abs" style="left:0;top:1032px" width="743" height="168" viewBox="0 0 743 168">
    <polygon points="0,52 743,0 743,168 0,168" fill="#0a5aa0"/>
    <polygon points="0,53 743,13 743,168 0,168" fill="#000000"/>
  </svg>

  <div class="abs contact" style="left:111px">
    <div class="contact-icon"><svg width="14" height="14" viewBox="0 0 14 14"><path d="M3 1.5l2 2.5-1.2 1.5c.8 1.8 2.2 3.2 4 4l1.5-1.2 2.5 2-1 2c-5 0-9.8-4.8-9.8-9.8z" fill="none" stroke="#fff" stroke-width=".9"/></svg></div>
    <div><div class="contact-label">PHONE</div><div class="contact-value">123-456-7890</div></div>
  </div>
  <div class="abs contact" style="left:262px">
    <div class="contact-icon"><svg width="14" height="14" viewBox="0 0 14 14"><path d="M7 13s4-4.5 4-7.5a4 4 0 0 0-8 0C3 8.5 7 13 7 13z" fill="none" stroke="#fff" stroke-width=".9"/><circle cx="7" cy="5.5" r="1.5" fill="none" stroke="#fff" stroke-width=".9"/></svg></div>
    <div><div class="contact-label">ADDRESS</div><div class="contact-value small">123 Lorem ipsum dolor sit amet,<br>consectetuer adipiscing.</div></div>
  </div>
  <div class="abs contact" style="left:480px">
    <div class="contact-icon"><svg width="14" height="14" viewBox="0 0 14 14"><rect x="1.5" y="5" width="11" height="7.5" fill="none" stroke="#fff" stroke-width=".9"/><polyline points="1.5,5 7,1.5 12.5,5" fill="none" stroke="#fff" stroke-width=".9"/><polyline points="1.5,5.5 7,9 12.5,5.5" fill="none" stroke="#fff" stroke-width=".9"/></svg></div>
    <div><div class="contact-label">EMAIL</div><div class="contact-value">info@halvernbuilders.com</div></div>
  </div>

  <div class="abs rule"></div>
  <p class="abs copyright">Copyright © 2021 <b>HALVERN BUILDERS.</b> All Rights Reserved.</p>
</div>
</body>
</html>
```